Gift Voucher For Medical Cosmetic Clinic

I need a high end, beautiful gift voucher for my Cosmetic Medical Clinic that I will provide to customers in a beautifully designed envelope. I like the colours blue with different tones of blue, white and silver. I have attached my business card for further information.
The address is: 3/14 Dunmore Lane, Ferrymead, Christchurch 8023.
Phone: 0800-457-839
Email: mirel@tovanu.co.nz
Website: www.tovanu.co.nz

```html
<!DOCTYPE html>
<html lang="en">
<head>
<meta charset="utf-8">
<title>Tovanu Gift Voucher and Envelope</title>
<link rel="stylesheet" href="https://fonts.googleapis.com/css2?family=Arimo:wght@400&family=Roboto+Condensed:wght@300;400&display=swap">
<style>
  :root {
    --backdrop: #2b2b2d;
    --blue-deep: #1874be;
    --blue-mid: #3796d3;
    --blue-light: #4eaee3;
    --blue-pale: #5fb9ea;
    --silver-dark: #a9abae;
    --silver: #cfd0d2;
    --silver-light: #f4f4f5;
    --ink: #1e1e1e;
    --ink-soft: #333;
    --white: #ffffff;
  }
  * { box-sizing: border-box; margin: 0; padding: 0; }
  html, body { width: 1200px; height: 563px; overflow: hidden; background: var(--backdrop); }
  .canvas { position: relative; width: 1200px; height: 563px; }

  /* Voucher front */
  .voucher {
    position: absolute; left: 78px; top: 64px; width: 485px; height: 434px;
    background: linear-gradient(160deg, var(--blue-mid) 0%, var(--blue-light) 70%, var(--blue-pale) 100%);
    overflow: hidden;
  }
  .brand-plate {
    position: absolute; left: 84px; top: 102px; width: 315px; height: 94px;
    background: linear-gradient(90deg, var(--blue-pale) 0%, var(--blue-mid) 60%, var(--blue-deep) 100%);
    display: flex; align-items: center; gap: 18px; padding-left: 26px;
  }
  .brand-plate .brand-dot {
    width: 62px; height: 62px; border-radius: 50%;
    border: 2px solid var(--silver);
  }
  .brand-name {
    font-family: "Roboto Condensed", sans-serif; font-weight: 300;
    color: var(--white); font-size: 44px; letter-spacing: 6px; line-height: 1;
  }
  .offer-band {
    position: absolute; left: 0; top: 300px; width: 100%; height: 22px;
    background: linear-gradient(180deg, var(--silver-dark), var(--silver));
  }
  .offer-title {
    position: absolute; left: 19px; top: 303px;
    font-family: "Arimo", sans-serif; font-weight: 400; font-size: 13px; line-height: 16px;
    color: var(--ink); letter-spacing: -0.2px; white-space: nowrap;
  }
  .treatments-panel {
    position: absolute; left: 0; top: 322px; width: 100%; height: 112px;
    background: linear-gradient(180deg, var(--silver-light) 0%, var(--silver) 60%, var(--silver-light) 100%);
  }
  .treatment-list {
    position: absolute; left: 19px; top: 343px; list-style: none;
    font-family: "Roboto Condensed", sans-serif; font-weight: 400; font-size: 10.5px;
    line-height: 16px; color: var(--ink-soft);
  }
  .treatment-row { display: flex; gap: 7px; height: 24px; white-space: nowrap; }
  .treatment-row span::before { content: "\2713"; margin-right: 11px; color: var(--ink); }
  .bow-artwork {
    position: absolute; left: 311px; top: 279px; width: 161px; height: 127px;
    border-radius: 40% 40% 30% 30%;
    background: radial-gradient(ellipse at 50% 40%, var(--silver-light) 0%, var(--silver) 60%, rgba(207,208,210,0) 100%);
  }

  /* Envelope */
  .envelope {
    position: absolute; left: 638px; top: 65px; width: 485px; height: 434px;
    background: linear-gradient(225deg, var(--blue-light) 0%, var(--blue-mid) 50%, var(--blue-deep) 100%);
    overflow: hidden;
  }
  .envelope-flap { position: absolute; left: 0; top: 0; width: 485px; height: 124px; }
  .envelope-plate {
    position: absolute; left: 154px; top: 31px; width: 177px; height: 53px;
    background: linear-gradient(90deg, var(--blue-pale), var(--blue-mid));
    display: flex; align-items: center; gap: 10px; padding-left: 10px;
  }
  .envelope-plate .brand-dot {
    width: 36px; height: 36px; border-radius: 50%; border: 1.5px solid var(--silver);
  }
  .envelope-plate .brand-name { font-size: 26px; letter-spacing: 3px; }
</style>
</head>
<body>
<main class="canvas">

  <section class="voucher" aria-label="Gift voucher front">
    <div class="brand-plate">
      <div class="brand-dot"></div>
      <div class="brand-name">TOVANU</div>
    </div>

    <div class="offer-band"></div>
    <div class="treatments-panel"></div>
    <h1 class="offer-title">TOVANU- YOUR LOCAL COSMETIC CLINIC</h1>
    <ul class="treatment-list">
      <li class="treatment-row"><span>Dermal Injectables</span><span>Plasma Facials</span><span>Microneedling</span></li>
      <li class="treatment-row"><span>Skin Boosters</span><span>Excessive Sweating</span></li>
    </ul>

    <div class="bow-artwork" role="img" aria-label="Silver satin ribbon bow"></div>
  </section>

  <section class="envelope" aria-label="Voucher envelope">
    <svg class="envelope-flap" viewBox="0 0 485 124" aria-hidden="true">
      <defs>
        <linearGradient id="flapTone" x1="0" y1="0" x2="1" y2="0">
          <stop offset="0" stop-color="#56b2e6"/>
          <stop offset="0.6" stop-color="#2f8dce"/>
          <stop offset="1" stop-color="#0f6fb7"/>
        </linearGradient>
      </defs>
      <path d="M0 0 H485 V77 Q485 124 438 124 H47 Q0 124 0 77 Z" fill="url(#flapTone)"/>
    </svg>
    <div class="envelope-plate">
      <div class="brand-dot"></div>
      <div class="brand-name">TOVANU</div>
    </div>
  </section>

</main>
</body>
</html>
```